Personal training studio poster / postcard

We need a poster / postcard design to advertise our recently established personal training studio - details and logo in the attached file. Logo file also provided.

We are flexible on format. Prefer the use of pictures in the design.

Training

```html
<!DOCTYPE html>
<html lang="en">
<head>
<meta charset="utf-8">
<title>Kensworth Strength Studio – Class Times</title>
<link rel="stylesheet" href="https://fonts.googleapis.com/css2?family=Pathway+Gothic+One&display=swap">
<style>
  :root {
    --bg: #000000;
    --band-light: #bdbaba;
    --band-mid: #7d7b7c;
    --band-dark: #3b3b3d;
    --number-light: #d6d4d4;
    --number-shade: #8e8c8d;
    --text-white: #ffffff;
    --tagline: #d9d9d9;
    --brand-silver: #c9c9cb;
    --swoosh: #1c1c1e;
    --pebble-light: #8a8a8c;
    --pebble-dark: #2c2c2e;
  }
  html, body {
    margin: 0;
    padding: 0;
    background: var(--bg);
    overflow: hidden;
  }
  .poster {
    position: relative;
    width: 1200px;
    height: 848px;
    background: var(--bg);
    overflow: hidden;
    font-family: "Pathway Gothic One", "Arial Narrow", sans-serif;
  }
  .swooshes {
    position: absolute;
    inset: 0;
  }
  .brand {
    position: absolute;
    left: 54px;
    top: 40px;
    width: 330px;
  }
  .brand-name {
    display: flex;
    align-items: center;
    gap: 12px;
    margin: 0;
    padding-left: 24px;
    font-size: 44px;
    font-weight: 400;
    line-height: 1;
    color: var(--brand-silver);
    letter-spacing: 1px;
  }
  .brand-mark {
    width: 18px;
    height: 18px;
    border-radius: 50%;
    background: var(--brand-silver);
    flex: none;
  }
  .brand-sub {
    margin: 8px 0 0 74px;
    font-size: 31px;
    line-height: 1;
    color: var(--brand-silver);
    letter-spacing: 2px;
  }
  .tagline {
    position: absolute;
    left: 54px;
    top: 164px;
    margin: 0;
    font-size: 19px;
    color: var(--tagline);
    white-space: nowrap;
  }
  .session {
    position: absolute;
    right: 0;
    background: linear-gradient(90deg, var(--band-light) 0%, var(--band-mid) 35%, var(--band-dark) 80%);
    border-radius: 6px 0 0 6px;
  }
  .session-number {
    position: absolute;
    top: 50%;
    transform: translateY(-50%);
    font-size: 300px;
    line-height: 1;
    color: var(--number-light);
    text-shadow: 4px 3px 0 var(--number-shade);
  }
  .session-time {
    position: absolute;
    margin: 0;
    font-size: 68px;
    font-weight: 400;
    line-height: 1.08;
    color: var(--text-white);
  }
  .session-icon {
    position: absolute;
    border-radius: 46% 54% 50% 50% / 50% 46% 54% 50%;
    background: radial-gradient(circle at 35% 30%, var(--pebble-light) 0%, var(--pebble-dark) 75%);
    box-shadow: 0 3px 8px rgba(0,0,0,0.5);
  }
  .session--one { top: 122px; left: 520px; height: 204px; }
  .session--one .session-number { left: -66px; }
  .session--one .session-time { left: 44px; top: 56px; }
  .session--one .session-icon { left: 460px; top: 14px; width: 176px; height: 176px; }

  .session--two { top: 335px; left: 440px; height: 222px; }
  .session--two .session-number { left: -70px; }
  .session--two .session-time { left: 118px; top: 32px; }
  .session--two .session-icon { left: 540px; top: 20px; width: 176px; height: 184px; }

  .session--three { top: 568px; left: 360px; height: 240px; }
  .session--three .session-number { left: -80px; }
  .session--three .session-time { left: 196px; top: 82px; }
  .session--three .session-icon { left: 638px; top: 28px; width: 158px; height: 178px; }
</style>
</head>
<body>
<main class="poster">
  <svg class="swooshes" width="1200" height="848" viewBox="0 0 1200 848" aria-hidden="true">
    <path d="M0 560 C 250 500, 600 470, 1200 520" fill="none" stroke="var(--swoosh)" stroke-width="14"/>
    <path d="M0 620 C 300 560, 700 560, 1200 600" fill="none" stroke="var(--swoosh)" stroke-width="8"/>
    <path d="M0 760 C 200 700, 420 690, 700 730" fill="none" stroke="var(--swoosh)" stroke-width="10"/>
  </svg>

  <header class="brand">
    <h1 class="brand-name"><span class="brand-mark"></span>KENSWORTH</h1>
    <p class="brand-sub">STRENGTH STUDIO</p>
  </header>
  <p class="tagline">Boutique personal and small group training studio</p>

  <section class="session session--one" style="right:0">
    <span class="session-number">1</span>
    <h2 class="session-time">Tuesdays 6:15am</h2>
    <div class="session-icon" role="img" aria-label="Icon of a person lifting dumbbells"></div>
  </section>

  <section class="session session--two">
    <span class="session-number">2</span>
    <h2 class="session-time">Tuesdays &amp;<br>Thursdays 6:15pm</h2>
    <div class="session-icon" role="img" aria-label="Icon of a person stretching over an exercise ball"></div>
  </section>

  <section class="session session--three">
    <span class="session-number">3</span>
    <h2 class="session-time">Saturdays 9am</h2>
    <div class="session-icon" role="img" aria-label="Icon of a person kicking a punching bag"></div>
  </section>
</main>
</body>
</html>
```